Brochure Design- Targeted at Property Developers

We are the largest Conveyancing (property law) firm in the state of Victoria, Australia.

We need a very sophisticated brochure to enable us to take the next step and compete with law firms for property developer clients.

Much about us can be found on our website (inlcuding logos, photos, etc) www.trellowby.com.au but our business name is Trellowby- Marsh Vale not just Trellowby. ALSO I HAVE ATTACHED MANY PHOTOS OF OUR STAFF AND SOME LOGOS TO HELP!!

Size: fold (A3 double sided so that there is 4 A4 pages)

Copy:

This can be played with by the designer to spread across the 4 pages. Ideally the front page will be very minimalistic and not mention our brand (or at least the brand should not dominate):

Page 1: Do property developers have a genuine alternative to high legal fees?

Page 2 and 3:

- 100% of our developer clients recommend us
- We already look after the Conveyancing needs of more developers in Victoria than any other Conveyancing firm
- Industry benchmark off- the- plan contracts (tailored to the requirements of each development). Our special conditions (including variations, rebates and resale restrictions) are carefully chosen to protect the interests of our vendors while being commercially sensitive to ensure sales are not lost unnecessarily
- Expert in guiding developers from first time dual occupancies to seasoned developers of large scale land and highrise projects
- Our large team and highly refined systems ensure fastest possible settlement times after subdivision registration
- We are available to train your project marketers on completing and executing contracts so that sales are not delayed or lost
- Establishment of interest bearing trust accounts
- Before you buy a development site have us thoroughly investigate the contract and vendors statement. We can then conduct the purchase settlement on your behalf.
- We have the friendliest and most efficient staff. Every dealing you have with our dedicated Development Division will be prompt, professional and impressive. You will never need to follow us up!
- Highly experienced Conveyancers with the security of full Solicitor support

Please consider us next time you need Conveyancing.

Services options:
- Use us from contract preparation to settlement or;
- Have your Solicitor prepare the contract and use us as an alternative for the settlement stage only. Many Solicitors recommend us for this service already
- Fast subdivision lodgements (including obtaining mortgagee’s consent, Solicitor preparation of Land Titles Office application, owners corporation establishment)

Page 4: Just our contact details (see our website)

The design should make us look highly professional, conservative, yet cutting edge.

Target Market(s)

Property developers of small to medium sized land and unit developments

Industry/Entity Type

Security

Requirements
Must have
• - Our logo and contact details as well as the copy above.
Nice to have
• - Pictures of land sites, highrise buildings under construction
Should not have
• I really dislike overly corny photos where everyone is fake and smiling. Other photos would be great but not too cheesy.

```html
<!DOCTYPE html>
<html lang="en">
<head>
<meta charset="utf-8">
<title>Trellowby- Marsh Vale — Developer Conveyancing Specialists</title>
<link href="https://fonts.googleapis.com/css2?family=Arimo:wght@400;700&family=Tinos:ital,wght@1,700&display=swap" rel="stylesheet">
<style>
  :root{
    --brand-blue:#1c1e9c;
    --ink:#1b1b1b;
    --paper:#f7f7fb;
    --paper-tint:#e9eaf4;
    --sky-deep:#3f7fc4;
    --sky-light:#bcd9f2;
    --grass:#7fae4a;
    --steel:#8c98a6;
  }
  *{margin:0;padding:0;box-sizing:border-box}
  html,body{width:1200px;height:849px;overflow:hidden;background:var(--paper)}
  .spread{position:relative;width:1200px;height:849px;
    background:linear-gradient(135deg,var(--paper) 0%,var(--paper-tint) 100%);
    font-family:"Arimo",Arial,sans-serif;color:var(--ink);overflow:hidden}

  .brand-block{position:absolute;left:71px;top:71px;width:253px;height:114px;background:var(--brand-blue);color:#fff}
  .brand-name{position:absolute;left:0;right:0;top:0;height:83px;display:flex;align-items:center;justify-content:center;gap:9px;
    font-family:"Arimo",Arial,sans-serif;font-weight:700;font-size:19px;color:#fff}
  .brand-square{width:12px;height:12px;background:#fff;flex:none}
  .brand-tag{position:absolute;left:0;right:0;bottom:0;height:31px;border-top:1px solid #fff;text-align:center;
    font-family:"Tinos","Times New Roman",serif;font-style:italic;font-weight:700;font-size:14px;line-height:30px}

  .benefits{position:absolute;left:72px;top:199px;width:262px;list-style:none}
  .benefits li{position:relative;padding-left:12px;font-size:11.5px;line-height:15.8px;margin-bottom:8px}
  .benefits li::before{content:"";position:absolute;left:0;top:6px;width:4px;height:4px;border-radius:50%;background:var(--ink)}

  .promise{position:absolute;left:74px;top:700px;width:290px;color:var(--brand-blue);
    font-family:"Tinos","Times New Roman",serif;font-style:italic;font-weight:700;font-size:13.6px;line-height:18.3px}
  .promise .mark{font-size:19px;line-height:0}

  .photo{position:absolute}
  .photo-call{left:374px;top:0;width:225px;height:357px;background:linear-gradient(160deg,#2d2522 0%,#b88f78 45%,#e3d8cf 65%,#1e1a18 100%)}
  .photo-sale{left:374px;top:360px;width:225px;height:147px;background:linear-gradient(180deg,#dfe9ef 0%,#a9c77a 45%,var(--grass) 100%)}
  .photo-tower{left:601px;top:0;width:343px;height:507px;background:linear-gradient(160deg,var(--sky-light) 0%,var(--sky-deep) 45%,#1f4f8a 100%)}
  .photo-frame{left:945px;top:330px;width:255px;height:177px;background:linear-gradient(180deg,#cfe0ef 0%,#7f9f5e 35%,var(--steel) 100%)}
  .photo-build{left:374px;top:510px;width:225px;height:339px;background:linear-gradient(180deg,#cfe2f3 0%,#8fb3d6 50%,#5b6770 85%,#3c4a3a 100%)}

  .invite{position:absolute;left:650px;top:540px;color:var(--brand-blue);
    font-family:"Tinos","Times New Roman",serif;font-style:italic;font-weight:700;font-size:20.5px;line-height:24.5px}
  .services-title{position:absolute;left:650px;top:600px;font-size:14.5px;font-weight:400}
  .services{position:absolute;left:660px;top:624px;width:250px;list-style:none}
  .services li{position:relative;padding-left:12px;font-size:11.5px;line-height:14.6px;margin-bottom:10px}
  .services li.nested{margin-left:11px}
  .services li::before{content:"";position:absolute;left:0;top:5px;width:4px;height:4px;border-radius:50%;background:var(--ink)}

  .phone{position:absolute;left:923px;top:792px;color:var(--brand-blue);font-weight:700;font-size:21.5px}
</style>
</head>
<body>
<main class="spread">
  <header class="brand-block">
    <div class="brand-name"><span class="brand-square"></span>Trellowby- Marsh Vale</div>
    <div class="brand-tag">Developer Conveyancing Specialists</div>
  </header>

  <ul class="benefits">
    <li>100% of our developer clients recommend us.</li>
    <li>We already look after the Conveyancing needs of more developers in Victoria than any other Conveyancing firm.</li>
    <li>Industry benchmark off-the-plan contracts (tailored to the requirements of each development). Our special conditions (including variations, rebates and resale restrictions) are carefully chosen to protect the interests of our vendors while being commercially sensitive to ensure sales are not lost unnecessarily.</li>
    <li>Expert in guiding developers from first time dual occupancies to seasoned developers of large scale land and highrise projects.</li>
    <li>Our large team and highly refined systems ensure fastest possible settlement times after subdivision registration.</li>
    <li>We are available to train your project marketers on completing and executing contracts so that sales are not delayed or lost.</li>
    <li>Establishment of interest bearing trust accounts.</li>
    <li>Before you buy a development site have us thoroughly investigate the contract and vendors statement. We can then conduct the purchase settlement on your behalf.</li>
    <li>Highly experienced Conveyancers with the security of full Solicitor support.</li>
  </ul>

  <blockquote class="promise"><span class="mark">“</span>We have the friendliest and most efficient<br>staff. Every dealing you have with our<br>dedicated Development Division will be<br>prompt, professional and impressive.<br>You will never need to follow us up!<span class="mark">”</span></blockquote>

  <div class="photo photo-call" role="img" aria-label="Photo of a staff member on a desk telephone"></div>
  <div class="photo photo-sale" role="img" aria-label="Photo of a for sale sign on a grassy land site"></div>
  <div class="photo photo-tower" role="img" aria-label="Photo of glass highrise towers against a blue sky"></div>
  <div class="photo photo-frame" role="img" aria-label="Photo of a steel roof frame under construction"></div>
  <div class="photo photo-build" role="img" aria-label="Photo of highrise buildings under construction with cranes"></div>

  <h2 class="invite">Please consider us next time<br>you need Conveyancing.</h2>
  <p class="services-title">Services options:</p>
  <ul class="services">
    <li>Use us from contract preparation to settlement or;</li>
    <li class="nested">Have your Solicitor prepare the contract and use us as an alternative for the settlement stage only. Many Solicitors recommend us for this service already.</li>
    <li class="nested">Fast subdivision lodgements (including obtaining mortgagee’s consent, Solicitor preparation of Land Titles Office application, owners corporation establishment).</li>
  </ul>

  <p class="phone">Phone: (03) 9412 7730</p>
</main>
</body>
</html>
```